Coffee and hot drinks advert on A-Board

Creative eye catching design to advertise coffee and hot drinks on an A-Board.

To use images and modern design to reflect the quality and almost specialist coffee house style drinks on offer.
We use organic milk and have had our own 'Larkfield Restaurant' coffee beans roasted to produce the perfect coffee.
We also use only the best hot chocolate and fresh cream to serve quality drinks.
All staff are barista trained.

Target Market(s)

Passing trade and coffee lovers for takeaway drinks

Industry/Entity Type

Coffee Shop

Font styles to use
Serif

Requirements
Must have
• Bold creative modern look.
• Independent coffee shop style look
• Mention we use 'Bramblewick Organic milk'
• We use our own roasted special blend of coffee
• speciality hot chocolate
Nice to have
• modern approach
• eye catching
Should not have
• complicated
• difficult to read
• old fashioned

```html
<!DOCTYPE html>
<html lang="en">
<head>
<meta charset="utf-8">
<title>Larkfield Restaurant – Takeaway Drinks A-Board</title>
<link rel="stylesheet" href="https://fonts.googleapis.com/css2?family=Cabin+Sketch:wght@700&family=Cabin:wght@400;500&family=Kalam:wght@400&family=Dosis:wght@400;500&display=swap">
<style>
  :root {
    --backdrop: #d9d9d6;
    --board: #1c1e1e;
    --board-light: #2c2f2f;
    --chalk: #ecebe4;
    --chalk-soft: #b9b8b2;
    --aqua: #7fd8dc;
    --lemon: #e8e47a;
  }
  * { margin: 0; padding: 0; box-sizing: border-box; }
  html, body {
    width: 1200px;
    height: 900px;
    overflow: hidden;
    background: var(--backdrop);
  }
  .canvas {
    position: relative;
    width: 1200px;
    height: 900px;
  }
  .aboard {
    position: absolute;
    left: 308px;
    top: 20px;
    width: 584px;
    height: 860px;
    background: radial-gradient(ellipse at 45% 40%, var(--board-light) 0%, var(--board) 70%);
    color: var(--chalk);
    font-family: "Cabin", sans-serif;
  }
  .aboard__frame {
    position: absolute;
    inset: 0;
  }
  .aboard__title {
    position: absolute;
    top: 34px;
    left: 50%;
    transform: translateX(-50%);
    padding: 0 14px;
    background: var(--board);
    font-family: "Cabin Sketch", cursive;
    font-weight: 700;
    font-size: 35px;
    letter-spacing: 1px;
    white-space: nowrap;
    line-height: 1;
  }
  .aboard__tagline {
    position: absolute;
    top: 122px;
    width: 100%;
    text-align: center;
    font-family: "Dosis", sans-serif;
    font-size: 22px;
    letter-spacing: 4px;
    text-transform: uppercase;
  }
  .aboard__tagline .highlight {
    color: var(--aqua);
    font-size: 27px;
  }
  .menu {
    position: absolute;
    top: 208px;
    left: 35px;
    right: 68px;
  }
  .menu__heading {
    text-align: center;
    color: var(--aqua);
    font-size: 20px;
    font-weight: 500;
    margin-bottom: 14px;
  }
  .menu__list { list-style: none; }
  .menu__item {
    display: flex;
    align-items: baseline;
    height: 39.6px;
    font-size: 19px;
  }
  .menu__leader {
    flex: 1;
    border-bottom: 2px dotted var(--chalk-soft);
    margin: 0 6px;
    transform: translateY(-4px);
  }
  .menu__price { font-weight: 500; }
  .menu__size { color: var(--chalk-soft); font-weight: 400; margin: 0 3px; }
  .menu__note {
    color: var(--chalk-soft);
    font-size: 18px;
    line-height: 37px;
    margin-top: 2px;
  }
  .promise {
    position: absolute;
    left: 38px;
    top: 660px;
    font-family: "Kalam", cursive;
    font-size: 29px;
    line-height: 40px;
  }
  .promise__milk {
    position: absolute;
    left: 38px;
    top: 730px;
    font-family: "Dosis", sans-serif;
    font-size: 19px;
    letter-spacing: 3px;
    text-transform: uppercase;
  }
  .promise__milk .lead { color: var(--lemon); }
  .promise__milk .brand { color: var(--aqua); }
  .beach-sketch {
    position: absolute;
    left: 385px;
    top: 632px;
    width: 128px;
    height: 126px;
    border-radius: 10px;
    background: radial-gradient(circle at 45% 50%, rgba(127,216,220,0.45) 0%, rgba(127,216,220,0.12) 60%, rgba(127,216,220,0) 80%);
  }
</style>
</head>
<body>
<main class="canvas">
  <section class="aboard">
    <svg class="aboard__frame" width="584" height="860" viewBox="0 0 584 860" aria-hidden="true">
      <rect x="16" y="52" width="552" height="786" fill="none" stroke="var(--chalk)" stroke-width="5" opacity="0.9"/>
      <rect x="30" y="66" width="524" height="758" fill="none" stroke="var(--chalk)" stroke-width="6" stroke-dasharray="14 9" opacity="0.85"/>
    </svg>

    <h1 class="aboard__title">LARKFIELD RESTAURANT</h1>

    <p class="aboard__tagline">Grab our <span class="highlight">Takeaway</span> drinks!</p>

    <div class="menu">
      <h2 class="menu__heading">Hot Drinks</h2>
      <ul class="menu__list">
        <li class="menu__item"><span>Pot of Tea</span><span class="menu__leader"></span><span class="menu__price">£1.30</span></li>
        <li class="menu__item"><span>Cappuccino</span><span class="menu__leader"></span><span class="menu__price"><span class="menu__size">Reg</span>£1.80 <span class="menu__size">Lrg</span>£2.20</span></li>
        <li class="menu__item"><span>Americano</span><span class="menu__leader"></span><span class="menu__price">£1.60</span></li>
        <li class="menu__item"><span>Latte</span><span class="menu__leader"></span><span class="menu__price">£1.75</span></li>
        <li class="menu__item"><span>Mocha</span><span class="menu__leader"></span><span class="menu__price">£1.80</span></li>
        <li class="menu__item"><span>Espresso</span><span class="menu__leader"></span><span class="menu__price">£1.20</span></li>
        <li class="menu__item"><span>Hot Chocolate</span><span class="menu__leader"></span><span class="menu__price">£1.80</span></li>
        <li class="menu__item"><span>Fine Teas</span><span class="menu__leader"></span><span class="menu__price">£2.00</span></li>
      </ul>
      <p class="menu__note">Earl Grey, English Breakfast, Jasmine Green, Citrus Mint<br>&amp; Raspberry Nectar</p>
    </div>

    <p class="promise">Coffee Beans,<br>roasted to perfection.</p>
    <p class="promise__milk"><span class="lead">We use</span> <span class="brand">Bramblewick Organic</span> milk!</p>

    <div class="beach-sketch" role="img" aria-label="Chalk sketch of a seaside bucket and spade on a little wave"></div>
  </section>
</main>
</body>
</html>
```